Cercle doré
Zielgruppe
Branche: klassische Musik; Musikgruppe: Klaviertrio (Geige, Cello, Klavier) Gesucht wird ein Flyer, den wir zur Aussendarstellung nutzen können. Zielgruppe sind Veranstalter von klassisch-konservativen Konzerten. Inhalt: Fotos der 3 MusikerInnen, 3x Porträtfoto, 1 Gesamtfoto, 3 Biografien, 1 Text zu unserem Klaviertrio. Der Flyer soll hauptsächlich per mail versandt werden, eine geringe Stückzahl soll ausgedruckt werden.
Format: DIN lang105 QUER !! 210 x 105 mm Vorder- und Rückseite ODER:
DIN lang 105 quer Einbruchfalz
Aufgabenstellung
Das Klaviertrio heisst "Cercle doré", wir spielen hauptsächlich klassisch-romantische Werke. Das Design sollte klassisch-romantisch, aber nicht zu verschnörkelt sein.

```html
<!DOCTYPE html>
<html lang="de">
<head>
<meta charset="utf-8">
<title>Cercle doré – Klaviertrio</title>
<link href="https://fonts.googleapis.com/css2?family=Playball&family=Alegreya:wght@400;500&display=swap" rel="stylesheet">
<style>
  :root {
    --page: #ffffff;
    --wine: #3c090a;
    --ivory: #ffffff;
    --photo-light: #e4e6e8;
    --photo-mid: #9a6a4a;
    --photo-dark: #2a3a36;
  }
  * { margin: 0; padding: 0; box-sizing: border-box; }
  html, body { width: 1200px; height: 600px; overflow: hidden; background: var(--page); }
  .flyer { position: relative; width: 1200px; height: 600px; }
  .band {
    position: absolute; left: 0; top: 18px; width: 1200px; height: 556px;
    background: var(--wine);
  }
  .ensemble-name {
    position: absolute; left: 0; top: 14px; width: 560px; text-align: center;
    font-family: "Playball", cursive; font-size: 68px; color: var(--ivory);
    line-height: 1.2;
  }
  .group-photo {
    position: absolute; left: 0; top: 114px; width: 552px; height: 372px;
    background: linear-gradient(100deg, var(--photo-dark) 0%, var(--photo-mid) 45%, var(--photo-light) 100%);
  }
  .instruments {
    position: absolute; left: 0; top: 492px; width: 580px; text-align: center;
    font-family: "Playball", cursive; font-size: 44px; color: var(--ivory);
    line-height: 1.2;
  }
  .copy {
    position: absolute; left: 580px; top: 78px; width: 590px; text-align: center;
    font-family: "Alegreya", serif; color: var(--ivory);
  }
  .quote { font-size: 29px; font-weight: 500; line-height: 46px; }
  .quote-author { font-size: 29px; font-weight: 500; line-height: 46px; }
  .about { margin-top: 52px; font-size: 26px; line-height: 52.5px; }
</style>
</head>
<body>
<div class="flyer">
  <div class="band"></div>
  <h1 class="ensemble-name">Cercle doré</h1>
  <div class="group-photo" role="img" aria-label="Gruppenfoto der drei Musiker mit Geige und Cello"></div>
  <p class="instruments">Geige, Cello, Klavier</p>
  <div class="copy">
    <p class="quote">„Musik ist der Raum zwischen den Noten“</p>
    <p class="quote-author">Clément Duvernay</p>
    <p class="about">
      Das Klaviertrio „Cercle doré“ spielt die<br>
      berühmtesten Werke aus der Romantik wie<br>
      Brandauer, Meinhardt-Bartok, Rachelnikov,<br>
      Rosenfeld und Tscherkassow.<br>
      Die Resonanz des Publikums:<br>
      genussvoll begeistert!
    </p>
  </div>
</div>
</body>
</html>
```